Plakat-Design für Veltrana
Zielgruppe
Wir sind eine 'kreative' kleine Truppe, die mit neuen Ideen versuchen wollen, auch mal andere Wege in den Projekten zu gehen.
Aufgabenstellung
Für die Motivation meiner Mitarbeiter und für meinen Empfang suche ich Plakate in der Höhe von ca. 150 cm und Breite von etwa 50 cm.
Sie sollen die weißen Wände etwas auflockern, von daher hätte ich gern die Hauptfarbe im Hintergrund. Ansonsten bitte für die Farbakzente die CD-Farben nutzen.
Grundsätzlich soll das Thema "Einfach Machen" sein. Ich möchte damit animieren Dinge und Wege auszuprobieren, ohne vorab immer scheu davor zu haben.
Gerne auch mit weiteren Textvorschlägen. Pro neuen Text, der dann auf ein Poster kommt, zahle ich einen Bonus von 40€.

```html
<!DOCTYPE html>
<html lang="de">
<head>
<meta charset="utf-8">
<title>Veltrana – Einfach machen</title>
<link href="https://fonts.googleapis.com/css2?family=Barlow:wght@400;600;700&display=swap" rel="stylesheet">
<style>
  :root {
    --bg: #434b4e;
    --accent: #ee5f73;
    --text-grey: #b5b7b9;
    --logo-light: #dde3e6;
  }
  html, body {
    margin: 0;
    padding: 0;
    width: 1200px;
    height: 3598px;
    overflow: hidden;
    background: var(--bg);
  }
  .poster {
    position: relative;
    width: 1200px;
    height: 3598px;
    background: var(--bg);
    font-family: "Barlow", sans-serif;
    text-align: center;
    overflow: hidden;
  }
  .headline {
    position: absolute;
    top: 606px;
    left: 0;
    width: 100%;
    margin: 0;
    font-size: 236px;
    line-height: 245px;
    font-weight: 700;
    color: var(--accent);
    letter-spacing: 4px;
    text-transform: uppercase;
  }
  .message {
    position: absolute;
    top: 1150px;
    left: 0;
    width: 100%;
    margin: 0;
    font-size: 100px;
    line-height: 136px;
    font-weight: 600;
    color: var(--text-grey);
    letter-spacing: 2px;
    text-transform: uppercase;
  }
  .tagline {
    position: absolute;
    top: 3143px;
    left: 0;
    width: 100%;
    margin: 0;
    font-size: 64px;
    line-height: 64px;
    font-weight: 400;
    color: var(--text-grey);
    letter-spacing: 2px;
    text-transform: uppercase;
  }
  .brand {
    position: absolute;
    top: 3270px;
    left: 0;
    width: 100%;
    margin: 0;
    font-size: 220px;
    line-height: 220px;
    font-weight: 400;
    color: var(--logo-light);
    letter-spacing: 2px;
  }
</style>
</head>
<body>
  <main class="poster">
    <h1 class="headline">I have<br>a dream</h1>
    <p class="message">Du bist ein Genie,<br>wenn du deinen<br>Träumen folgst.</p>
    <p class="tagline">Einfach machen!</p>
    <p class="brand">Veltrana</p>
  </main>
</body>
</html>
```